Lotvantage.com Webpage Design

Design Brief for lotvantage.com (Copy of Brief also in attached Word file)

Name of Website- lotvantage.com (existing logo and look & feel of website to be changed)

Logo - Finalised. The logo files are attached with the brief as “logo.jpeg”. The “Blue- Grey” version of the logo is for use on lighter backgrounds and the “Orange-White” version of the logo is for use on darker backgrounds. (A full Black version of the logo is also attached). Both versions may be used in different parts of the website. All attached files are in .png format.
Status - The website in functional and is undergoing user trials. However, we want to improve the look & feel of the website so at it seems
a. cotemporary,
b. Easy to Navigate
c. professional and
d. Vibrant.

Please visit ‘lotvantage.com’ to check out the website and its functionalities – please use it only as a reference for the features & functions to be provided, however the designer should use a ‘Free Hand’ in designing the composition of various parts of the webpage without getting too influenced by the existing design

Objective of the Website ‘lotvantage.com –
a. It is a portal focussed on listing of ‘Retail’ specific real-estate properties by developers, owners and realty brokers. The properties shall listed under the following four categories-
i. Retail Malls
ii. Shopping Complexes
iii. High-street shops
iv. Retail Warehouses
*refer lotvantage.com for better clarity

b. The abovementioned properties shall be listed either for ‘Sale’ or ‘rent\lease’ or both

c. Users shall visit the site in case they wish to acquire a retail \ shop space either on ‘sale’ or ‘rent’. These Users would be able to specify the ‘Search Criteria’ through the tool-bars provided on the website – the ‘Search Criteria’ shall comprise of ‘Type of space category’, ‘City’, ‘Locality’, transaction type ie ‘Rent \ Sale’ and ‘Area Range’

d. The main revenue model for the website shall be listing fee ( or advertising charges ) payable by those listing their properties on the website.

Three Main Pages of Website (lotvantage.com) that need to be designed -
a. Main Home Page (visit the web link - http://lotvantage.com/ ) - The main home page has the “Search Toolbar” for specifying of Search Criteria by the User. It shall also have the following features & functions-
i. Main Advertising Banner
ii. Featured Projects
iii. New Launches
iv. Toolbar with buttons – ‘Advertise with Us’, ‘Listings Alert’, ‘Lot Mavens’, ‘Advertiser Login’

b. Property Listings Page (visit the web link - http://lotvantage.com/gurgaon-in-india ) - The List of property options that match the Criteria specified by the ‘User’ get displayed on this page.

c. Property Detail Page - When the ‘User’ clicks on the “More….” Button on the ‘Property Listings Page’ (given in point b. above) the web page with the details of the property opens. (For Example – visit the web link - http://lotvantage.com/brevo-Shopping-Complex-brevo-quadrel-gurgaon-636 )

Note:- Please refer to attached ‘Shopping’ related images the designer may use them on the website to provide a look & feel of retail if required – either separately or rotate in a single window

Target Market(s)

Retailers & Investors looking for retail space, Real Estate Brokers, Developers

Industry/Entity Type

Advertising

Number of Pages Required

3 page

Requirements
Must have
• Refer to existing site lotvantage.com -- all the existing functionalities are a must have.
Nice to have
• The Designer may use the retail related images on the website if required for making it more vibrant. Refer attached images Shopping(1-6).jpg

```html
<!DOCTYPE html>
<html lang="en">
<head>
<meta charset="utf-8">
<title>Lotvantage.com – Contact</title>
<link href="https://fonts.googleapis.com/css2?family=Fira+Sans:wght@400;500;600&display=swap" rel="stylesheet">
<style>
  :root {
    --page-bg: #ffffff;
    --field-bg: #d6d6d6;
    --field-text: #3a3a3a;
    --heading-text: #2b2b2b;
    --accent-teal: #1a9aac;
    --footer-bg: #121212;
    --footer-text: #ffffff;
    --link-blue: #1f9be3;
    --brand-orange: #f5a623;
    --social-one: #4f73b7;
    --social-two: #5ec9ef;
    --social-three: #ee6363;
    --social-four: #1d88c8;
    --social-five: #444446;
    --map-green: #d5e4c0;
    --map-grey: #e8e6e0;
  }
  * { box-sizing: border-box; margin: 0; padding: 0; }
  html, body { width: 1200px; height: 533px; overflow: hidden; background: var(--page-bg); }
  body { position: relative; font-family: "Fira Sans", sans-serif; color: var(--heading-text); }

  .contact-heading, .side-heading {
    position: absolute; top: -6px; font-size: 19px; font-weight: 400; color: var(--heading-text);
  }
  .contact-heading { left: 179px; }
  .side-heading { left: 728px; }

  .field {
    position: absolute; background: var(--field-bg); color: var(--field-text);
    font-size: 19px; padding-left: 31px; line-height: 48px;
  }
  .field-name { left: 179px; top: 46px; width: 224px; height: 48px; }
  .field-email { left: 425px; top: 46px; width: 224px; height: 48px; }
  .field-message { left: 179px; top: 116px; width: 470px; height: 132px; line-height: 1; padding-top: 20px; }

  .submit-button {
    position: absolute; left: 179px; top: 270px; width: 312px; height: 48px;
    background: var(--accent-teal); color: #fff; font-size: 22px; font-weight: 600;
    padding-left: 31px; line-height: 48px;
  }
  .submit-button svg { position: absolute; left: 249px; top: 6px; }

  .social-list { position: absolute; left: 728px; top: 46px; display: flex; gap: 13px; list-style: none; }
  .social-list li { width: 48px; height: 48px; }
  .social-one { background: var(--social-one); }
  .social-two { background: var(--social-two); }
  .social-three { background: var(--social-three); }
  .social-four { background: var(--social-four); }
  .social-five { background: var(--social-five); }

  .location-map {
    position: absolute; left: 728px; top: 116px; width: 294px; height: 202px;
    background: linear-gradient(135deg, var(--map-grey) 0%, var(--map-green) 100%);
  }

  .site-footer {
    position: absolute; left: 0; top: 358px; width: 1200px; height: 175px;
    background: var(--footer-bg); color: var(--footer-text); font-size: 12.5px; line-height: 15.8px;
  }
  .footer-links { position: absolute; top: 15px; list-style: none; }
  .footer-links-company { left: 179px; }
  .footer-links-categories { left: 273px; }
  .footer-about { position: absolute; left: 392px; top: 15px; width: 330px; }
  .footer-about a { color: var(--link-blue); text-decoration: none; }
  .copyright { position: absolute; left: 179px; top: 158px; color: var(--link-blue); }

  .brand-mark { position: absolute; left: 738px; top: 72px; display: flex; align-items: center; gap: 12px; }
  .brand-dot { width: 34px; height: 34px; border-radius: 50%; background: var(--brand-orange); }
  .brand-name { font-size: 36px; font-weight: 600; color: var(--footer-text); letter-spacing: -0.5px; }
</style>
</head>
<body>
  <h2 class="contact-heading">We Have Perfect Property for you</h2>
  <h2 class="side-heading">Lorem ipsum dolor sit amet,</h2>

  <form class="contact-form">
    <div class="field field-name">Name</div>
    <div class="field field-email">Email</div>
    <div class="field field-message">Message</div>
    <div class="submit-button">Submit
      <svg width="40" height="38" viewBox="0 0 40 38" aria-hidden="true">
        <polygon points="1,18 39,1 30,36 19,26" fill="#fff"/>
        <polygon points="19,26 39,1 15,24 16,36" fill="#d9eef1"/>
      </svg>
    </div>
  </form>

  <ul class="social-list" aria-label="Social links">
    <li class="social-one" aria-label="Social link one"></li>
    <li class="social-two" aria-label="Social link two"></li>
    <li class="social-three" aria-label="Social link three"></li>
    <li class="social-four" aria-label="Social link four"></li>
    <li class="social-five" aria-label="Social link five"></li>
  </ul>

  <div class="location-map" role="img" aria-label="Map showing the office location"></div>

  <footer class="site-footer">
    <ul class="footer-links footer-links-company">
      <li>About Us</li><li>Privacy Policy</li><li>Terms of Use</li><li>Contact Us</li><li>Site Map</li>
    </ul>
    <ul class="footer-links footer-links-categories">
      <li>Retail Malls</li><li>Shopping Complex</li><li>High Street Shops</li><li>Retail Warehouses</li>
    </ul>
    <p class="footer-about">www.lotvantage.com<br>Lotvantage.com - About Us Lotvantage.com is a Specialised Web based platform for Retail Space, featuring properties across India under various formats such as Retail Malls, Shopping Complexes, High-street Shops. Also featured are ‘Retail Warehouses’ which provide the logis-tic back-end for the retail business. Lotvantage.com as follows- a. Devel <a href="#">More...</a></p>
    <div class="brand-mark">
      <span class="brand-dot"></span>
      <span class="brand-name">Lotvantage</span>
    </div>
    <p class="copyright">Copyright © 2015 Bharat Retail Hub.com. All rights reserved.</p>
  </footer>
</body>
</html>
```